Fatigued and Overloaded by COVID Messages? We need original illustrations to show that.

Everywhere you look there are messages about COVID. That is leading many people to feel fatigued and overloaded by the messages.

We surveyed U.S. adults March 20th - 24th, 2020 and measured message fatigue, information overload, perceived repetition, and perceived exaggeration. Here is how participants responded:

When it comes to coronavirus . . .
55% feel exhausted by all the messages.
54% feel overloaded by the amount of information.
51% feel that the messages are repetitive.
47% feel like messages exaggerate how bad it is.

In other words, almost half of U.S. adults show signs of message fatigue, information overload, perceived message repetition, and perceived message exaggeration.

We will continue to survey 400 adults every week for the next 16 weeks. Each time we will measure message fatigue, information overload, perceived repetition, and perceived exaggeration. We expect that it will increase over time.

What are we looking for? We need innovative and original illustrations that attempt to communicate these findings. The illustrations would visualize message fatigue, information overload, perceived message repetition, and perceived message exaggeration.

What sort of visual are we looking for? Our preference is for an original illustration (or set of illustrations). Our preference is for creative and powerful illustrations, but we are also open to the creative and well-executed infographics.

We need these images fast . We will award monetary prizes to the 3 best designs. If we like more than that, then we might purchase more (e.g., in past contests, we have purchased as many as 30 designs).

What we will need:
(1) The illustrations must be original and we will need the photoshop and/or illustrator files for all artwork. (By original, we mean that the illustrations are 100% created by you. Our organization requires that we utilize only original illustrated work. We have had issues with free imagery being pirated and reposted as free. We sidestep that issue by just having everything created.)

(2) The illustration should say, somewhere: "Based on a survey of 400 U.S. adults conducted March 20 - 24th, 2020."

(3) We will have almost 4 months worth of data by the time this is done. In other words, the illustrations might be able to help us present that weekly data.

(4) We have conducted other Artvendo projects. It might be helpful to examine designs we liked in the past. For example, here is another COVID project we just finished:

https://jobs.artvendo-example.com/job/5162048

Target Market(s)

U.S. adults

Requirements
Must have
• Original illustrations. Mobile friendly design. People will view this on their smartphones.
Nice to have
• A design that we can use to communicate the data across time.

```html
<!DOCTYPE html>
<html lang="en">
<head>
<meta charset="utf-8">
<title>Coronavirus Message Fatigue</title>
<link href="https://fonts.googleapis.com/css2?family=Jost:wght@400;500;700;800&family=Nunito:wght@900&display=swap" rel="stylesheet">
<style>
  :root {
    --purple-top: #8a4f8c;
    --purple-deep: #5f2a6e;
    --purple-band: #642a7d;
    --orange: #f9a024;
    --tan: #e3c68d;
    --magenta: #a0004a;
    --lime: #d9dd22;
    --bar-blue: #4b78e6;
    --bar-track: #ece6d4;
    --ink: #111111;
    --white: #ffffff;
  }
  * { margin: 0; padding: 0; box-sizing: border-box; }
  html, body { width: 676px; height: 1200px; overflow: hidden; }
  body { font-family: "Jost", sans-serif; background: var(--purple-band); }
  .poster {
    position: relative; width: 676px; height: 1200px; overflow: hidden;
    background: linear-gradient(180deg, var(--purple-top) 0px, var(--purple-deep) 150px, var(--purple-band) 1000px);
  }
  .source-note {
    position: absolute; top: 36px; left: 0; width: 100%;
    text-align: center; color: var(--white);
    font-family: "Nunito", sans-serif; font-weight: 900;
    font-size: 16px; line-height: 22px; text-transform: uppercase; letter-spacing: 0.2px;
  }
  .intro-bar {
    position: absolute; top: 101px; left: 31px; width: 618px; height: 70px;
    background: #4e1d5c; border-radius: 22px;
  }
  .intro-bar h1 {
    position: absolute; top: 12px; left: 35px;
    font-family: "Nunito", sans-serif; font-weight: 900;
    font-size: 31px; color: var(--white); letter-spacing: 0.3px;
  }
  .stat {
    position: absolute; left: 0; width: 676px;
  }
  .stat--exhausted { top: 163px; height: 210px; background: var(--orange); border-radius: 36px 36px 0 0; }
  .stat--overloaded { top: 372px; height: 226px; background: var(--tan); }
  .stat--repetitive { top: 597px; height: 218px; background: var(--magenta); }
  .stat--exaggerated { top: 815px; height: 201px; background: var(--lime); }
  .stat__art {
    position: absolute; left: 8px; width: 255px;
  }
  .stat__bar {
    position: absolute; left: 287px; width: 313px; height: 71px;
    background: var(--bar-track);
  }
  .stat__fill {
    position: absolute; left: 0; top: 0; height: 100%;
    background: var(--bar-blue); border-radius: 0 36px 36px 0;
  }
  .stat__value {
    position: absolute; left: 14px; top: 4px;
    font-weight: 800; font-size: 54px; line-height: 62px; color: var(--white);
  }
  .stat__label {
    position: absolute; left: 288px; width: 380px;
    font-size: 31px; line-height: 42px; font-weight: 500; color: var(--ink); letter-spacing: 0.5px;
  }
  .stat--repetitive .stat__label { color: var(--white); }
  .summary {
    position: absolute; top: 1053px; left: 40px; width: 596px;
    text-align: center; color: var(--white); font-size: 19.5px; line-height: 28px;
  }
</style>
</head>
<body>
<main class="poster">
  <p class="source-note">"Based on a survey of 400 U.S. adults<br>conducted March 20 - 24th, 2020."</p>

  <div class="intro-bar"><h1>When it comes to coronavirus . . .</h1></div>

  <section class="stat stat--exhausted">
    <svg class="stat__art" style="top:27px;height:160px" viewBox="0 0 255 160" role="img" aria-label="Illustration of a drooping person weighed down by large speech bubbles marked with virus icons">
      <rect x="52" y="0" width="203" height="160" fill="#f6b24a"/>
    </svg>
    <div class="stat__bar" style="top:37px"><div class="stat__fill" style="width:57%"></div><span class="stat__value">55%</span></div>
    <p class="stat__label" style="top:110px">Feel exhausted by all<br>the messages.</p>
  </section>

  <section class="stat stat--overloaded">
    <svg class="stat__art" style="top:14px;height:200px" viewBox="0 0 255 200" role="img" aria-label="Illustration of a startled person buried under a long scroll of information">
      <rect x="52" y="20" width="203" height="180" fill="#dcbd80"/>
    </svg>
    <div class="stat__bar" style="top:28px"><div class="stat__fill" style="width:55%"></div><span class="stat__value">54%</span></div>
    <p class="stat__label" style="top:110px">Feel overloaded by the<br>amount of information.</p>
  </section>

  <section class="stat stat--repetitive">
    <svg class="stat__art" style="top:20px;height:180px" viewBox="0 0 255 180" role="img" aria-label="Illustration of a tired person beside a speech bubble circled by looping arrows">
      <rect x="52" y="0" width="203" height="180" fill="#93003f"/>
    </svg>
    <div class="stat__bar" style="top:27px"><div class="stat__fill" style="width:55%"></div><span class="stat__value">51%</span></div>
    <p class="stat__label" style="top:110px">Feel that the messages<br>are repetitive.</p>
  </section>

  <section class="stat stat--exaggerated">
    <svg class="stat__art" style="top:12px;height:180px" viewBox="0 0 255 180" role="img" aria-label="Illustration of a slumped person next to a chart with an exaggerated rising curve">
      <rect x="52" y="0" width="203" height="180" fill="#e0e23a"/>
    </svg>
    <div class="stat__bar" style="top:23px"><div class="stat__fill" style="width:50%"></div><span class="stat__value">47%</span></div>
    <p class="stat__label" style="top:103px">Feel like messages<br>exaggerate how bad it is.</p>
  </section>

  <p class="summary">In other words, almost half of U.S. adults show signs of message fatigue, information overload, perceived message repetition, and perceived message exaggeration.</p>
</main>
</body>
</html>
```